Vondelmar Silver Gifts needs an attractive PRODUCT catalog

We need a catalog for our products. We are manufacturers of fine sterling silver gifts. We sell baby gifts, mens gifts, entertaining gifts, etc. We need a simple, elegant and attractive catalog for our retailers to view our entire collection of products.
We need a simple yet impressive product catalog for our company. We sell silver gifts of all kinds and need to design a catalog with images, prices and information on our products to give our clients and sales rep. The primary purpose of the catalog is to showcase our products clearly. However we require a high end looking catalog to represent our product line. We have about 100- 150 products. We don't need something fancy where our product line is not clearly showcased. But a design factor to the catalog is what we are looking for.

We have our brand colors and logo.

Industry/Entity Type

Gift Shop

Font styles to use
Serif

Colors
ec1f27
ffffff
aaaaaa

Requirements
Must have
• An Introduction page
• A reference of categories by pages
• A photo, SKU, Price for each product
Nice to have
• A hint of our brand colors in a subtle way
Should not have
• Too much color

```html
<!DOCTYPE html>
<html lang="en">
<head>
<meta charset="utf-8">
<title>Vondelmar Silver Gifts – Catalog Spread</title>
<link rel="stylesheet" href="https://fonts.googleapis.com/css2?family=Lato:wght@300;400;700&display=swap">
<style>
  :root {
    --brand-red: #b01e24;
    --ink-dark: #3d3f41;
    --bar-grey: #a9a9a9;
    --title-grey: #9a9a9a;
    --body-grey: #a2a2a2;
    --paper: #fdfdfd;
    --backdrop: #e4e3df;
    --white: #ffffff;
  }
  * { box-sizing: border-box; margin: 0; padding: 0; }
  html, body { width: 1200px; height: 804px; overflow: hidden; }
  body {
    background: var(--backdrop);
    font-family: "Lato", Arial, sans-serif;
    position: relative;
  }
  .spread {
    position: absolute;
    left: 80px; top: 52px;
    width: 1040px; height: 700px;
    display: flex;
    box-shadow: 0 6px 24px rgba(0,0,0,.12);
  }
  .page {
    position: relative;
    width: 520px; height: 700px;
    overflow: hidden;
  }
  .page--left { background: linear-gradient(to right, #fafafa 0%, #fdfdfd 85%, #e9e9e9 100%); }
  .page--right { background: linear-gradient(to right, #e6e6e6 0%, #fbfbfb 12%, #fdfdfd 100%); }

  /* header */
  .header-band {
    position: absolute; top: 28px;
    width: 42px; height: 20px;
    background: var(--brand-red);
  }
  .page--left .header-band { left: 0; }
  .page--right .header-band { right: 0; }
  .header-tab {
    position: absolute; top: 28px;
    width: 26px; height: 20px;
    background: var(--ink-dark);
    transform: skewX(-20deg);
    display: flex; align-items: center; justify-content: center;
  }
  .page--left .header-tab { left: 36px; }
  .page--right .header-tab { right: 36px; }
  .brand {
    position: absolute; top: 24px;
    display: flex; align-items: center; gap: 6px;
  }
  .page--left .brand { left: 76px; }
  .page--right .brand { right: 82px; }
  .brand-dot {
    width: 16px; height: 16px; border-radius: 50%;
    background: var(--ink-dark);
  }
  .brand-name {
    font-size: 17px; font-weight: 400; letter-spacing: 1.5px;
    color: var(--ink-dark);
  }
  .header-rule {
    position: absolute; top: 38px; height: 1.5px;
    background: var(--ink-dark);
  }
  .page--left .header-rule { left: 212px; right: 22px; }
  .page--right .header-rule { left: 0; right: 236px; }

  /* titles */
  .page-title {
    position: absolute;
    font-size: 58px; font-weight: 300;
    color: var(--title-grey);
    letter-spacing: 1px;
  }
  .page--left .page-title { left: 150px; top: 140px; }
  .page--right .page-title { left: 62px; top: 108px; }

  /* contents list */
  .contents-list {
    position: absolute; left: 118px; top: 262px;
    list-style: none;
  }
  .contents-item {
    display: flex; align-items: center;
    height: 26px; margin-bottom: 11px;
  }
  .contents-num {
    width: 36px; height: 26px;
    background: var(--ink-dark); color: var(--white);
    font-size: 18px; font-weight: 700;
    display: flex; align-items: center; justify-content: center;
    border-radius: 2px;
  }
  .contents-label {
    width: 300px; height: 21px;
    background: var(--bar-grey); color: var(--white);
    font-size: 10.5px; font-weight: 400;
    display: flex; align-items: center;
    padding-left: 9px;
    border-radius: 0 4px 4px 0;
    margin-top: -4px;
    white-space: nowrap; overflow: hidden;
  }

  /* about body */
  .about-body {
    position: absolute; left: 62px; top: 208px; width: 410px;
    color: var(--body-grey);
    font-size: 9.6px; line-height: 13.5px; font-weight: 400;
  }
  .about-body p { margin-bottom: 13px; }

  /* footer */
  .footer {
    position: absolute; bottom: 0; left: 0; right: 0;
    height: 34px; display: flex;
  }
  .footer-web {
    width: 140px; background: var(--brand-red); color: var(--white);
    font-size: 10px; display: flex; align-items: center; justify-content: center;
  }
  .footer-bar {
    flex: 1; background: var(--ink-dark); color: var(--white);
    font-size: 9px; display: flex; align-items: center; justify-content: center;
    position: relative;
  }
  .page-num {
    position: absolute; top: 7px;
    width: 20px; height: 20px; border-radius: 50%;
    background: var(--white); border: 2px solid var(--brand-red);
    color: var(--ink-dark); font-size: 10px; font-weight: 700;
    display: flex; align-items: center; justify-content: center;
  }
  .page--left .page-num { right: 14px; }
  .page--right .page-num { left: 14px; }
</style>
</head>
<body>
  <main class="spread">
    <section class="page page--left" aria-label="Contents page">
      <div class="header-band"></div>
      <div class="header-tab">
        <svg width="12" height="12" viewBox="0 0 12 12" style="transform:skewX(20deg)"><circle cx="6" cy="6" r="5.5" fill="#fff"/><path d="M5 3.5 L7.5 6 L5 8.5" stroke="#b01e24" stroke-width="1.6" fill="none"/></svg>
      </div>
      <div class="brand"><span class="brand-dot"></span><span class="brand-name">vondelmar</span></div>
      <div class="header-rule"></div>

      <h1 class="page-title">Contents</h1>
      <ol class="contents-list">
        <li class="contents-item"><span class="contents-num">03</span><span class="contents-label">Baby Gifts – Cups, Rattles &amp; Spoons</span></li>
        <li class="contents-item"><span class="contents-num">04</span><span class="contents-label">Men’s Gifts – Cufflinks &amp; Money Clips</span></li>
        <li class="contents-item"><span class="contents-num">05</span><span class="contents-label">Entertaining – Trays, Bowls &amp; Barware</span></li>
        <li class="contents-item"><span class="contents-num">06</span><span class="contents-label">Frames &amp; Keepsakes</span></li>
        <li class="contents-item"><span class="contents-num">07</span><span class="contents-label">Home Accents &amp; Candlesticks</span></li>
        <li class="contents-item"><span class="contents-num">08</span><span class="contents-label">Holiday Ornaments</span></li>
        <li class="contents-item"><span class="contents-num">09</span><span class="contents-label">Personalised Engraving</span></li>
        <li class="contents-item"><span class="contents-num">10</span><span class="contents-label">Ordering, SKUs &amp; Price Guide</span></li>
      </ol>

      <footer class="footer">
        <div class="footer-web">www.vondelmar.com</div>
        <div class="footer-bar">Phone: 555.010.222 | info@vondelmar.com<span class="page-num">2</span></div>
      </footer>
    </section>

    <section class="page page--right" aria-label="About us page">
      <div class="header-rule"></div>
      <div class="brand"><span class="brand-dot"></span><span class="brand-name">vondelmar</span></div>
      <div class="header-tab">
        <svg width="12" height="12" viewBox="0 0 12 12" style="transform:skewX(20deg)"><circle cx="6" cy="6" r="5.5" fill="#fff"/><path d="M7 3.5 L4.5 6 L7 8.5" stroke="#b01e24" stroke-width="1.6" fill="none"/></svg>
      </div>
      <div class="header-band"></div>

      <h1 class="page-title">About Us</h1>
      <div class="about-body">
        <p>Some companies design their gifts, then work hard to convince you how much you need them. At Vondelmar, every piece begins with the moment it will mark—a birth, a toast, a milestone worth remembering for a lifetime.</p>
        <p>Our silversmiths work in fine sterling, shaping each cup, frame, rattle and cufflink before it is polished, inspected and wrapped by hand. Every item in this catalog is shown with its photograph, its own SKU and its retailer price, so you and your sales representatives can present the collection clearly and order with confidence and speed.</p>
        <p>The collection is arranged by category. Baby gifts open the catalog with cups, rattles and spoons (pg. 3). Men’s gifts follow with cufflinks, money clips and desk pieces (pg. 4), then entertaining pieces for the table and bar (pg. 5). Frames and keepsakes, home accents and holiday ornaments complete the range (pg. 6–8).</p>
        <p>Engraving options for every piece are described on page 9, and a full ordering guide with SKUs and prices for all one hundred fifty pieces closes the catalog. (pg. 10)</p>
      </div>

      <footer class="footer">
        <div class="footer-bar">Phone: 555.010.222 | info@vondelmar.com<span class="page-num">3</span></div>
        <div class="footer-web">www.vondelmar.com</div>
      </footer>
    </section>
  </main>
</body>
</html>
```